Corrigan Construction Law P.A.

Business Card with Corporate Logo. For a law firm specializing in construction law.

need address, telephone, email and website. Also, have an elegant and conservative logo.

Logo so it is RBN.

Full name "Gordon T. Corrigan

Under my name title "Attorney at Law"

Under title "Board Certified in Construction Law"

PA in email is lower case

Add logo to back side of card

Mix in a bit of gold color into card to go with the green

Some color on bottom
Updates

Target Market(s)

legal

Industry/Entity Type

Construction

Contact Information for Business Card

I like it -- edits: 1. add "L" to logo so it is RBN. 2. add my full name "Gordon T. Business Card with Corporate Logo. For a law firm specializing in construction law.

Logo so it is RBN.

PA in email is lower case

Font styles to use
Serif

Colors
00a990
f78f20

Requirements
Must have
• Conservative legal designed logo for construction market
• Address:
• Corrigan Construction Law, P.A.
• 4150 Meadowlark Ave North, Ste B4
• Jacksonville, Florida 32217
• Main: 904-555-3172
• Direct: 904-555-8410
• Fax: 904-555-8410
• gt@corriganpa-example.com
• www.corriganbuildlaw-example.com
Nice to have
• Catchy conservative logo on card
Should not have
• Flashy

```html
<!DOCTYPE html>
<html lang="en">
<head>
<meta charset="utf-8">
<title>Corrigan Construction Law – Business Card</title>
<link href="https://fonts.googleapis.com/css2?family=EB+Garamond:wght@400;500;600&display=swap" rel="stylesheet">
<style>
  :root {
    --page: #e4e4e4;
    --ink-dark: #1f2a27;
    --ink-mid: #3a4542;
    --ink-soft: #7d8784;
    --green: #00a990;
    --gold: #f78f20;
    --band-text: #ffffff;
  }
  * { box-sizing: border-box; margin: 0; padding: 0; }
  html, body {
    width: 1200px;
    height: 900px;
    overflow: hidden;
    background: var(--page);
    font-family: "EB Garamond", Georgia, serif;
  }
  .card {
    position: absolute;
    left: 150px;
    top: 190px;
    width: 900px;
    height: 520px;
    border-radius: 44px;
    overflow: hidden;
    box-shadow: 0 14px 36px rgba(0,0,0,0.22);
  }
  .card-shapes { position: absolute; inset: 0; }
  .brand {
    position: absolute;
    left: 84px;
    top: 56px;
    display: flex;
    align-items: center;
    gap: 16px;
  }
  .brand-dot {
    width: 22px;
    height: 22px;
    border-radius: 50%;
    background: var(--gold);
  }
  .brand-mark {
    font-size: 66px;
    line-height: 80px;
    font-weight: 600;
    color: var(--green);
    letter-spacing: 4px;
  }
  .firm-name {
    position: absolute;
    left: 84px;
    top: 150px;
    font-size: 32px;
    line-height: 40px;
    font-weight: 500;
    color: var(--ink-soft);
  }
  .person { position: absolute; left: 84px; top: 222px; }
  .person-name {
    font-size: 34px;
    line-height: 40px;
    font-weight: 500;
    color: var(--ink-dark);
    letter-spacing: 1px;
  }
  .person-title {
    margin-left: 14px;
    font-size: 22px;
    line-height: 28px;
    font-weight: 500;
    color: var(--ink-mid);
    letter-spacing: 1px;
  }
  .person-cert {
    margin-left: 14px;
    font-size: 17px;
    line-height: 24px;
    color: var(--ink-soft);
  }
  .address {
    position: absolute;
    left: 96px;
    top: 424px;
    font-size: 21px;
    line-height: 32px;
    color: var(--band-text);
  }
  .contacts {
    position: absolute;
    right: 48px;
    top: 130px;
    list-style: none;
    text-align: right;
    color: var(--band-text);
    font-size: 19px;
    line-height: 38px;
    letter-spacing: 0.5px;
  }
  .contacts li { display: flex; justify-content: flex-end; align-items: center; gap: 12px; }
  .contacts .icon { width: 20px; height: 20px; flex: none; }
</style>
</head>
<body>
  <div class="card">
    <svg class="card-shapes" viewBox="0 0 900 520" width="900" height="520" aria-hidden="true">
      <defs>
        <linearGradient id="face" x1="0" y1="0" x2="1" y2="1">
          <stop offset="0" stop-color="#f4f4f4"/>
          <stop offset="0.5" stop-color="#ffffff"/>
          <stop offset="1" stop-color="#dcdcdc"/>
        </linearGradient>
      </defs>
      <rect width="900" height="520" fill="url(#face)"/>
      <path d="M 0 384 C 250 390, 470 320, 548 170 C 578 110, 588 50, 580 0"
            fill="none" stroke="var(--gold)" stroke-width="8"/>
      <path d="M 600 0 L 900 0 L 900 520 L 0 520 L 0 400 C 260 400, 490 330, 566 180 C 596 120, 606 55, 600 0 Z"
            fill="var(--green)"/>
    </svg>

    <div class="brand">
      <span class="brand-dot"></span>
      <span class="brand-mark">RBN</span>
    </div>
    <div class="firm-name">Corrigan Construction Law, P.A.</div>

    <div class="person">
      <div class="person-name">Gordon T. Corrigan</div>
      <div class="person-title">Attorney at Law</div>
      <div class="person-cert">Board Certified in Construction Law</div>
    </div>

    <div class="address">
      4150 Meadowlark Ave North, Ste B4<br>
      Jacksonville, Florida 32217
    </div>

    <ul class="contacts">
      <li>904-555-3172
        <svg class="icon" viewBox="0 0 20 20"><path d="M5 2 L8 2 L9 6 L7 8 C8 11 9 12 12 13 L14 11 L18 12 L18 15 C18 17 16 18 14 18 C8 17 3 12 2 6 C2 4 3 2 5 2 Z" fill="#fff"/></svg>
      </li>
      <li>904-555-8410
        <svg class="icon" viewBox="0 0 20 20"><rect x="5" y="1" width="10" height="18" rx="2" fill="none" stroke="#fff" stroke-width="2"/><circle cx="10" cy="15.5" r="1.2" fill="#fff"/></svg>
      </li>
      <li>904-555-8410
        <svg class="icon" viewBox="0 0 20 20"><rect x="5" y="2" width="10" height="6" fill="#fff"/><rect x="2" y="8" width="16" height="8" rx="1" fill="#fff"/><rect x="5" y="13" width="10" height="5" fill="#fff" stroke="#00a990" stroke-width="1"/></svg>
      </li>
      <li>gt@corriganpa-example.com
        <svg class="icon" viewBox="0 0 20 20"><rect x="1" y="4" width="18" height="12" fill="#fff"/><path d="M1 4 L10 11 L19 4" fill="none" stroke="#00a990" stroke-width="1.5"/></svg>
      </li>
      <li>www.corriganbuildlaw-example.com
        <svg class="icon" viewBox="0 0 20 20"><circle cx="10" cy="10" r="8" fill="none" stroke="#fff" stroke-width="1.6"/><ellipse cx="10" cy="10" rx="3.5" ry="8" fill="none" stroke="#fff" stroke-width="1.4"/><path d="M2 10 H18 M3.5 6 H16.5 M3.5 14 H16.5" stroke="#fff" stroke-width="1.2"/></svg>
      </li>
    </ul>
  </div>
</body>
</html>
```